Varnel Supply requires a new business card.

We are an online professional tool store.

Target Market(s)

We target the professional technician.

Industry/Entity Type

Business

Contact Information for Business Card

VarnelSupply.com.au

sales@varnelsupply.example

Requirements
Must have
• Needs to look commercial and professional
Should not have
• No Australian Colors, maps or shapes.
• No Shapes of Tools

```html
<!DOCTYPE html>
<html lang="en">
<head>
<meta charset="utf-8">
<title>Varnel Supply – Business Card</title>
<link rel="stylesheet" href="https://fonts.googleapis.com/css2?family=Oswald:wght@600&family=Work+Sans:wght@400;500;600&display=swap">
<style>
  :root {
    --stage-top: #2b2b2b;
    --stage-bottom: #0c0c0c;
    --card: #1d1d1d;
    --card-edge: #262626;
    --silver: #c4c4c4;
    --silver-soft: #8a8a8a;
    --ink-deep: #0e0e0e;
    --rule: #4a4a4a;
  }
  * { margin: 0; padding: 0; box-sizing: border-box; }
  html, body { width: 1200px; height: 900px; overflow: hidden; }
  body {
    background: radial-gradient(ellipse at 50% 35%, var(--stage-top), var(--stage-bottom) 75%);
    font-family: "Work Sans", sans-serif;
    position: relative;
  }
  .card {
    position: absolute;
    left: 280px;
    width: 640px;
    height: 366px;
    background: linear-gradient(135deg, var(--card-edge), var(--card) 60%);
    box-shadow: 0 18px 40px rgba(0,0,0,0.55);
  }
  .card--front { top: 60px; }
  .card--back { top: 470px; }

  /* Front */
  .brand {
    position: absolute;
    top: 130px;
    left: 0;
    right: 0;
    display: flex;
    align-items: center;
    justify-content: center;
    gap: 16px;
  }
  .brand__dot {
    width: 40px;
    height: 40px;
    border-radius: 50%;
    background: var(--silver);
  }
  .brand__name {
    font-size: 50px;
    font-weight: 600;
    color: var(--silver);
    letter-spacing: 0.5px;
  }
  .front__url {
    position: absolute;
    bottom: 42px;
    width: 100%;
    text-align: center;
    font-size: 16px;
    color: var(--ink-deep);
    text-shadow: 0 1px 0 rgba(255,255,255,0.12);
    letter-spacing: 0.5px;
  }

  /* Back */
  .holder {
    position: absolute;
    top: 108px;
    right: 358px;
    text-align: right;
  }
  .holder__name {
    font-family: "Oswald", sans-serif;
    font-weight: 600;
    font-size: 36px;
    letter-spacing: 1px;
    color: var(--ink-deep);
    text-shadow: 0 1px 0 rgba(255,255,255,0.1), 0 -1px 0 rgba(0,0,0,0.6);
    line-height: 1.1;
  }
  .holder__role {
    font-size: 15px;
    letter-spacing: 1px;
    color: var(--ink-deep);
    text-shadow: 0 1px 0 rgba(255,255,255,0.1);
    margin-top: 4px;
  }
  .divider {
    position: absolute;
    top: 100px;
    left: 308px;
    width: 1px;
    height: 90px;
    background: var(--rule);
  }
  .contact {
    position: absolute;
    top: 100px;
    left: 330px;
    list-style: none;
  }
  .contact__item {
    display: flex;
    align-items: center;
    gap: 12px;
    font-size: 17px;
    color: var(--silver);
    height: 23px;
  }
  .contact__item svg { width: 13px; height: 13px; fill: var(--silver-soft); flex: none; }
  .location {
    position: absolute;
    left: 28px;
    bottom: 38px;
    font-size: 16px;
    color: var(--ink-deep);
    text-shadow: 0 1px 0 rgba(255,255,255,0.12);
    letter-spacing: 0.4px;
  }
  .location__value { color: var(--silver); text-shadow: none; }
</style>
</head>
<body>
  <section class="card card--front">
    <div class="brand">
      <span class="brand__dot"></span>
      <span class="brand__name">Varnel Supply</span>
    </div>
    <p class="front__url">www.VarnelSupply.com.au</p>
  </section>

  <section class="card card--back">
    <div class="holder">
      <p class="holder__name">DARREN HOLT</p>
      <p class="holder__role">FOUNDER</p>
    </div>
    <span class="divider"></span>
    <ul class="contact">
      <li class="contact__item">
        <svg viewBox="0 0 16 16" aria-hidden="true"><path d="M3 1l3 3-2 2c1 2 3 4 5 5l2-2 3 3-2 3C7 15 1 9 0 3z"/></svg>
        (555) 014-2290
      </li>
      <li class="contact__item">
        <svg viewBox="0 0 16 16" aria-hidden="true"><path d="M4 0h8v16H4zM5.5 2v10h5V2zM7 13.5h2v1H7z" fill-rule="evenodd"/></svg>
        (555) 014-7731
      </li>
      <li class="contact__item">
        <svg viewBox="0 0 16 16" aria-hidden="true"><path d="M0 3h16v10H0zM1.5 4.5L8 9l6.5-4.5" /></svg>
        sales@varnelsupply.example
      </li>
      <li class="contact__item">
        <svg viewBox="0 0 16 16" aria-hidden="true"><circle cx="8" cy="8" r="7"/><path d="M1 8h14M8 1v14" stroke="#1d1d1d" stroke-width="1.2"/></svg>
        VarnelSupply.com.au
      </li>
    </ul>
    <p class="location">Location: <span class="location__value">41 Corbel Lane, Marden TX 77210</span></p>
  </section>
</body>
</html>
```